Web Design Project

We are looking for a unified design of Corporate Website, Stationary (Including Letterhead and Envelopes), Business Cards, Email Footers and Sales & Marketing Brochures.

Color palette should include:
Black (R: 24, G:24, B:24)
Red (R:206, G:0, B:39)
Dark Grey (R:51, G:51, B:51)
Light Grey/Silver (R:203, G:203, B:203)

As we do business in North America and the UK, designs should be reflective of standard sizing for both regions.

Check out our website to better understand who we are: www.KLVT.com and a copy of our Logo has been uploaded for reference.
Updates

Hello all, we had not anticipated the volume of unique, high quality designs we have received, thank you all for your submissions. A team review of all designs will take place the week of December 8th, and final decisions and selections made. Thank you again

Target Market(s)

Automotive Parts Wholesalers, Vehicle Repair Specialists, Automotive Parts Manufacturers, Automotive Insurance

Industry/Entity Type

Business

Font styles to use
Sans Serif

Requirements
Must have
• - Color palette should include:
- Black (R: 24, G:24, B:24)
- Red (R:206, G:0, B:39)
- Dark Grey (R:51, G:51, B:51)
- Light Grey/Silver (R:203, G:203, B:203)
Should not have
• No Animations

```html
<!DOCTYPE html>
<html lang="en">
<head>
<meta charset="utf-8">
<title>Kelvate Parts Solutions</title>
<link href="https://fonts.googleapis.com/css2?family=Raleway:wght@400;500;600;700&family=Open+Sans:wght@400;600;700&display=swap" rel="stylesheet">
<style>
:root{
  --red:#ce0027;
  --black:#181818;
  --dark:#333333;
  --silver:#cbcbcb;
  --panel:#ececec;
  --white:#ffffff;
  --text:#3a3a3a;
  --muted:#777777;
}
*{margin:0;padding:0;box-sizing:border-box}
html,body{width:1200px;height:2601px;overflow:hidden;background:var(--white)}
body{position:relative;font-family:"Open Sans",Arial,sans-serif;color:var(--text)}
.abs{position:absolute}

/* header */
.site-header{position:absolute;left:0;top:0;width:1200px;height:116px;border-top:5px solid var(--red);background:var(--white)}
.brand{position:absolute;left:55px;top:32px;display:flex;align-items:center;gap:12px}
.brand-mark{width:52px;height:52px;border-radius:50%;background:var(--silver)}
.brand-name{font-family:"Raleway",sans-serif;font-weight:700;font-size:25px;line-height:1;color:var(--dark)}
.brand-name small{display:block;font-size:15px;font-weight:400;letter-spacing:2px;color:var(--muted);margin-top:3px}
.top-links{position:absolute;right:26px;top:5px;display:flex;align-items:center;font-size:12px;gap:14px}
.top-links .region{color:var(--muted)}
.top-links .region.active{color:var(--red)}
.top-links .login{background:var(--red);color:var(--white);padding:4px 10px;margin-left:24px}
.top-links .awards{background:#e6e6e6;color:var(--dark);padding:4px 10px;margin-left:-14px}
.main-nav{position:absolute;right:26px;top:58px;display:flex;gap:32px;font-family:"Raleway",sans-serif;font-size:14px;font-weight:500;color:var(--black);align-items:center}
.main-nav .current{background:var(--red);color:var(--white);padding:6px 14px}

/* hero */
.hero{position:absolute;left:0;top:116px;width:1200px;height:591px;background:linear-gradient(135deg,#2a2a2a 0%,#6b6b6b 45%,#9a9a9a 60%,#3c3c3c 100%)}
.hero-card{position:absolute;left:55px;top:127px;width:362px;height:390px;background:rgba(206,0,39,.93);padding:40px 42px;color:var(--white)}
.hero-card h1{font-family:"Raleway",sans-serif;font-weight:700;font-size:31px;line-height:38px;margin-bottom:26px}
.hero-card li{list-style:none;font-family:"Raleway",sans-serif;font-size:18px;line-height:30px;margin-bottom:16px;text-transform:uppercase}
.hero-dots{position:absolute;left:55px;top:532px;display:flex;gap:4px}
.hero-dots span{width:8px;height:8px;background:#b0b0b0}
.hero-dots span:first-child{background:var(--red)}
.hero-progress{position:absolute;left:0;top:585px;width:590px;height:6px;background:var(--red)}

/* make strip */
.makes{position:absolute;left:0;top:707px;width:1200px;height:99px;display:flex;justify-content:center;align-items:center;gap:22px}
.makes span{width:34px;height:34px;border-radius:50%;background:var(--silver)}

/* about */
.band-grey{position:absolute;left:0;top:806px;width:1200px;height:874px;background:var(--panel)}
.video{position:absolute;left:52px;top:872px;width:442px;height:290px;background:linear-gradient(180deg,#1c1c1c,#4a3a28 55%,#111)}
.video-bar{position:absolute;left:52px;top:1134px;width:442px;height:28px;background:#1a1a1a;border-top:4px solid var(--red);color:#ccc;font-size:10px;display:flex;align-items:center;padding-left:116px}
.about{position:absolute;left:564px;top:893px;width:520px}
.about h2{font-family:"Raleway",sans-serif;font-weight:400;font-size:26px;color:var(--red);margin-bottom:16px}
.about p{font-size:14px;line-height:23px;color:var(--text)}
.about .more{display:block;color:var(--red);font-size:12px;margin-top:20px}

.cards{position:absolute;left:52px;top:1226px;display:flex;gap:15px}
.card{width:262px;height:390px;background:var(--white);border-top:4px solid var(--red);border-bottom:4px solid var(--red);box-shadow:0 2px 4px rgba(0,0,0,.15)}
.card-photo{height:187px}
.card h3{font-family:"Raleway",sans-serif;font-weight:400;font-size:22px;line-height:26px;color:var(--red);padding:18px 22px 10px}
.card p{font-size:12px;line-height:19px;padding:0 22px;color:var(--text)}
.photo-gears{background:linear-gradient(135deg,#d8d8d8,#6a6a6a)}
.photo-plugs{background:linear-gradient(135deg,#2a7fd0,#b9c4cc)}
.photo-engine{background:linear-gradient(135deg,#c6c9cc,#55595d)}
.photo-bay{background:linear-gradient(135deg,#8a9096,#2c3034)}
.awards-badge{position:absolute;margin:52px 0 0 36px;width:190px;height:80px;background:var(--white);display:flex;align-items:center;justify-content:center;gap:8px;font-family:"Raleway",sans-serif;font-weight:700;font-size:17px;color:var(--red)}
.awards-badge i{width:26px;height:26px;border-radius:50%;background:var(--red)}

/* references */
.refs{position:absolute;left:52px;top:1720px;width:680px}
.refs h2{font-family:"Raleway",sans-serif;font-weight:400;font-size:22px;color:var(--red);margin-bottom:10px}
.refs h4{font-size:14px;font-weight:700;color:var(--black);margin-bottom:4px}
.refs p{font-size:13px;line-height:21px}
.avatar{position:absolute;left:976px;top:1726px;width:144px;height:144px;border-radius:50%;background:#efefef}
.select-label{position:absolute;left:52px;top:1874px;font-size:14px;font-weight:600;color:var(--black)}
.select-row{position:absolute;top:1911px;display:flex;align-items:center;gap:12px;font-size:13px}
.select-box{width:292px;height:30px;background:#ededed;display:flex;align-items:center;justify-content:space-between;padding:0 14px;font-size:13px}
.pager{position:absolute;left:1100px;top:1972px;display:flex;gap:12px;font-size:20px;color:var(--black)}
.quote{position:absolute;left:52px;top:2006px;width:1087px;height:158px;display:flex}
.quote-who{width:294px;background:#eaeaea;padding:26px 0 0 28px}
.quote-who b{display:block;color:var(--red);font-size:13px}
.quote-who span{font-size:13px;color:var(--black)}
.quote-photo{width:160px;background:linear-gradient(135deg,#c9b8a6,#6f7b86)}
.quote-text{flex:1;background:var(--red);color:var(--white);font-size:13px;line-height:22px;padding:32px 70px 0 58px;position:relative}
.quote-text svg{position:absolute}

/* footer */
.site-footer{position:absolute;left:0;top:2223px;width:1200px;height:378px;background:var(--dark);border-top:4px solid var(--red)}
.foot-left{position:absolute;left:16px;top:0;width:348px;height:374px;background:var(--white);padding:26px 0 0 42px;font-size:12px;line-height:18px;color:var(--black)}
.foot-left .brand{position:static;margin-bottom:18px}
.foot-left h5{color:var(--red);font-size:14px;margin-bottom:4px}
.cols2{display:flex;gap:50px;margin-top:14px}
.foot-col{position:absolute;top:50px;width:230px;font-size:12px;line-height:19px;color:#e0e0e0}
.foot-col h5{color:var(--red);font-size:13px;font-weight:600;margin-bottom:8px}
.foot-col b{color:var(--white)}
.news input{width:210px;height:30px;background:#5a5a5a;border:0;color:#ccc;padding:0 10px;font-size:12px}
.news .btn{display:inline-block;margin-top:12px;background:var(--red);color:var(--white);padding:5px 16px;font-weight:600}
.social{display:flex;gap:8px;margin-top:4px}
.social span{width:24px;height:24px;border-radius:50%;background:#1b74c9}
.copyright{position:absolute;left:420px;top:332px;font-size:11px;color:#8a8a8a}
</style>
</head>
<body>

<header class="site-header">
  <div class="brand"><span class="brand-mark"></span><div class="brand-name">KELVATE<small>parts solutions</small></div></div>
  <div class="top-links">
    <span class="region">CDN</span><span class="region">UK</span><span class="region active">USA</span>
    <span class="login">Supplier Login</span><span class="awards">Kelvate Awards</span>
  </div>
  <nav class="main-nav">
    <span class="current">Home</span><span>Intelligent Sales &amp; Marketting</span><span>Kelvate Awards</span><span>References</span><span>About us</span><span>Careers</span><span>Contacts</span>
  </nav>
</header>

<section class="hero" role="img" aria-label="Close-up photograph of an engine belt and pulley">
  <div class="hero-card">
    <h1>Genuine Parts<br>Sales &amp; Marketting</h1>
    <ul>
      <li>Drive new and incremental parts sales</li>
      <li>2500 dealer clients</li>
      <li>Singular automotive focus</li>
      <li>Best in class service</li>
    </ul>
  </div>
  <div class="hero-dots"><span></span><span></span><span></span><span></span></div>
  <div class="hero-progress"></div>
</section>

<div class="makes" aria-label="Vehicle makes represented">
  <span></span><span></span><span></span><span></span><span></span><span></span><span></span><span></span><span></span><span></span><span></span><span></span><span></span><span></span><span></span><span></span><span></span><span></span><span></span><span></span>
</div>

<div class="band-grey"></div>
<div class="video" role="img" aria-label="Video still of engine pistons lit in warm light"></div>
<div class="video-bar">1:00 / 1:00</div>
<section class="about">
  <h2>About Us</h2>
  <p>Since 1988 we have provided wholesale parts sales and marketing solutions to automotive parts, services and repairer networks throughout Canada, USA and UK.<br>We represent over 2,500 OE parts and services suppliers to our network of over 400,000 independent repairer businesses.</p>
  <span class="more">more...</span>
</section>

<div class="cards">
  <article class="card">
    <div class="card-photo photo-gears" role="img" aria-label="Photograph of a gearbox with metal gears"></div>
    <h3>The Opportunity</h3>
    <p>OE Wholesale Parts provide significant opportunities for both OE dealership suppliers and repairers to capture new and incremental profits...</p>
  </article>
  <article class="card">
    <div class="card-photo photo-plugs" role="img" aria-label="Photograph of spark plugs on a blue background"></div>
    <h3>The Kelvate Multi-Brand Solution</h3>
    <p>We offer a unique multi-brand solution to both OE suppliers and the automotive repairers by combining professionally managed parts programs that are shared...</p>
  </article>
  <article class="card">
    <div class="card-photo photo-engine" role="img" aria-label="Photograph of an engine block">
      <div class="awards-badge"><i></i>Kelvate Awards</div>
    </div>
    <h3>Kelvate Parts Rewards</h3>
    <p>Our Kelvate Awards wholesale parts loyalty program is designed specifically for the automotive repair industry. Repairers earn Reward Points from multiple</p>
  </article>
  <article class="card">
    <div class="card-photo photo-bay" role="img" aria-label="Photograph of an engine bay"></div>
    <h3>services include</h3>
    <p>Professional Wholesale Parts Business Development Managers, One-to-One Email / Web Marketing, National Parts Locator Service, National OE Parts Rewards Loyalty Program...</p>
  </article>
</div>

<section class="refs">
  <h2>Client References</h2>
  <h4>Our Wholesale Parts Solutions References</h4>
  <p>Since 1988 we've earned the trust from thousands of our clients making us the leader in providing OE wholesale parts sales and marketing solutions. We are very proud to have provided them with the best service we can offer. See what they have to say.</p>
</section>
<div class="avatar" role="img" aria-label="Client testimonial icon"></div>
<div class="select-label">Please Select Region and Franchise:</div>
<div class="select-row" style="left:52px">Region <div class="select-box">North America (English) <span>&#8964;</span></div></div>
<div class="select-row" style="left:444px">Franchise <div class="select-box">North America (English) <span>&#8964;</span></div></div>
<div class="pager"><span style="color:#bbb">&#8249;</span><span>&#8250;</span></div>

<div class="quote">
  <div class="quote-who"><b>Dale Hosking - Parts Director</b><span>NORVIK MOTORS CLEVELAND</span></div>
  <div class="quote-photo" role="img" aria-label="Portrait photograph of the parts director"></div>
  <div class="quote-text">
    <svg style="left:8px;top:0" width="40" height="34" viewBox="0 0 40 34"><path d="M0 34V16L10 0h6L9 16h8v18zM22 34V16L32 0h6l-7 16h8v18z" fill="#fff"/></svg>
    Tom Bremer is an asset to your company &amp; our business. He works diligently on our behalf. He is "hands on" when it comes to representing us to outside wholesale shops. He knows our business well and supports all programs from our manufacturers. I look forward to his weekly visits.
    <svg style="right:8px;bottom:0" width="40" height="34" viewBox="0 0 40 34"><path d="M40 0v18L30 34h-6l7-16h-8V0zM18 0v18L8 34H2l7-16H1V0z" fill="#fff"/></svg>
  </div>
</div>

<footer class="site-footer">
  <div class="foot-left">
    <div class="brand"><span class="brand-mark"></span><div class="brand-name">KELVATE<small>parts solutions</small></div></div>
    <h5>Canada</h5>
    <b>GLOBAL OPERATIONS</b><br>Kelvate DataSystems<br>Corporation<br>Suite 210 - 4470 Harbour Way,<br>Burnaby, British Columbia,<br>Canada V5B 2K4
    <div class="cols2"><div><b>Toll Free</b><br>800.555.0142</div><div><b>Telephone</b><br>604.555.0187</div></div>
    <div class="cols2"><div><b>Fax:</b><br>800.555.0163</div><div><b>Email</b><br>info@kelvate-ds.com</div></div>
  </div>
  <div class="foot-col" style="left:420px">
    <h5>U.S.A</h5>
    Kelvate DataSystems<br>Corporation<br>1450 Ridgeline Ave NE<br>Suite 300, Building C<br>Bellevue, Washington<br>USA 98005
    <div class="cols2" style="gap:40px"><div><b>Toll Free</b><br>800.555.0142</div><div><b>Fax:</b><br>800.555.0163</div></div>
    <div style="margin-top:10px"><b>Email</b><br>info@kelvate-ds.com</div>
  </div>
  <div class="foot-col" style="left:677px">
    <h5>United Kingdom</h5>
    Kelvate DS Ltd.<br>Mill House<br>12 Orchard Road<br>Hinckley<br>Leicestershire, UK<br>LE10 3XY
    <div class="cols2" style="gap:20px"><div><b>Telephone</b><br>01455.555012</div><div><b>Fax:</b><br>01455.555034</div></div>
    <div style="margin-top:10px"><b>Email</b><br>enquiriesuk@kelvate-ds.com</div>
  </div>
  <div class="foot-col news" style="left:935px">
    <h5>News Letter</h5>
    <input type="text" value="Email" aria-label="Email">
    <span class="btn">Subscribe</span>
    <h5 style="margin-top:40px">Follow Us</h5>
    <div class="social"><span></span><span></span><span></span><span></span></div>
  </div>
  <div class="copyright">Copyright © 1998 - 2014 Kelvate Parts Solutions</div>
</footer>

</body>
</html>
```